wine label for ultra premium vineyard in Bendigo, Central Otago, New Zealand

"LARKSPUR" is our new wine brand, with grapes grown in our spectacular "ter Hoeven" vineyard. The small, elevated vineyard overlooks a river valley and snowy mountains. We would like a highly elegant label for our 2018 pinot noir wine, which highlights the quality of wine and our very special vineyard location. "LARKSPUR" has to be prominent, with secondary emphasis on "ter Hoeven vineyard" and "Bendigo, Central Otago". A stylized LARKSPUR logo (bird) could be a useful design device instead of the commonly seen illustrated mountain landscape (which is quite common for our local wines). Label size 90 high, 110 wide. Please use a pinot noir / burgundy bottle. See here for vineyard pics, and also below pics for other local wine labels and pics for inspiration / styles. https://www.instagram.com/jas.ter.hoeven.example/

Target Market(s)

average bottle price for this premium red pinot noir would be aroundUS$40. target market are generally urban professionals aged 25 and older with a high degree of interest in pinot noir wine, and who are familiar with New Zealand pinot noir (ie. already know several brands).

Colors
ed252d

Requirements
Must have
• distinctive label, sophisticated look
Nice to have
• classy white paper stock
Should not have
• label must not get too busy... less but high quality and distinctive is more....

```html
<!DOCTYPE html>
<html lang="en">
<head>
<meta charset="utf-8">
<title>LARKSPUR — ter Hoeven Vineyard Pinot Noir 2018 Label</title>
<link rel="stylesheet" href="https://fonts.googleapis.com/css2?family=Bodoni+Moda:opsz,wght@6..96,400&family=Marcellus&display=swap">
<style>
  :root {
    --brand-red: #ed252d;
    --brand-red-soft: #f2626b;
    --paper: #ffffff;
    --backdrop: #141012;
    --emblem-dark: #1d1b1e;
    --emblem-grey: #8f95a8;
    --emblem-orange: #e8691a;
  }
  html, body {
    margin: 0;
    padding: 0;
    width: 1156px;
    height: 1200px;
    overflow: hidden;
    background: var(--backdrop);
  }
  .canvas {
    position: relative;
    width: 1156px;
    height: 1200px;
  }
  .label {
    position: absolute;
    left: 38px;
    top: 158px;
    width: 1080px;
    height: 884px;
    background: var(--paper);
    color: var(--brand-red);
    font-family: "Marcellus", "Times New Roman", serif;
    overflow: hidden;
  }
  .label__brand {
    position: absolute;
    top: 52px;
    left: 0;
    width: 100%;
    margin: 0;
    text-align: center;
    font-family: "Bodoni Moda", "Didot", serif;
    font-weight: 400;
    font-size: 176px;
    line-height: 1;
    letter-spacing: -2px;
  }
  .label__band {
    position: absolute;
    left: 0;
    top: 258px;
    width: 100%;
    height: 277px;
    background: linear-gradient(100deg, var(--brand-red-soft) 0%, #ef4149 45%, var(--brand-red) 100%);
  }
  .label__emblem {
    position: absolute;
    left: 395px;
    top: 52px;
    width: 283px;
    height: 163px;
    border-radius: 60% 45% 40% 50%;
    background: linear-gradient(120deg, var(--emblem-dark) 0%, var(--emblem-grey) 45%, var(--emblem-orange) 80%);
  }
  .label__vineyard,
  .label__region,
  .label__vintage,
  .label__variety {
    position: absolute;
    margin: 0;
    line-height: 1;
    white-space: nowrap;
  }
  .label__vineyard {
    left: 129px;
    top: 576px;
    font-size: 46px;
    letter-spacing: 1px;
  }
  .label__region {
    left: 511px;
    top: 640px;
    font-size: 33px;
  }
  .label__vintage {
    left: 0;
    width: 100%;
    text-align: center;
    top: 736px;
    font-size: 34px;
  }
  .label__rule {
    position: absolute;
    left: 0;
    top: 784px;
    width: 100%;
    height: 25px;
    background: linear-gradient(90deg, var(--brand-red-soft) 0%, var(--brand-red) 35%, #f0454d 60%, var(--brand-red-soft) 100%);
  }
  .label__variety {
    left: 0;
    width: 100%;
    text-align: center;
    top: 830px;
    font-size: 34px;
  }
</style>
</head>
<body>
  <main class="canvas">
    <section class="label" aria-label="Wine label">
      <h1 class="label__brand">LARKSPUR</h1>
      <div class="label__band">
        <div class="label__emblem" role="img" aria-label="Stylised illustration of a small perched songbird with grey back, black cap and orange breast"></div>
      </div>
      <p class="label__vineyard">TER HOEVEN VINEYARD</p>
      <p class="label__region">BENDIGO, CENTRAL OTAGO</p>
      <p class="label__vintage">-2018-</p>
      <div class="label__rule"></div>
      <p class="label__variety">PINOT NOIR</p>
    </section>
  </main>
</body>
</html>
```